Anzeigengestaltung für ambulanten Pflegedienst
Zielgruppe
Es handelt sich um einen ambulanten Pflegedienst, der am 01. September 2024 einjähriges Jubiläum feiert. Von 10:00 Uhr bis 15:00 Uhr ist dazu im Büro in der Lindenweg 14 in Dessau-Roßlau ein kleiner Empfang mit Kuchen und Getränken geplant.
Weiterhin benötige ich eine Anzeige, um einen Hauswirtschafter zu suchen.
Und eine Anzeige für Beratungen gem.

```html
<!DOCTYPE html>
<html lang="de">
<head>
<meta charset="utf-8">
<title>Sorgsam Pflege – Anzeigen</title>
<link rel="stylesheet" href="https://fonts.googleapis.com/css2?family=Quicksand:wght@500;600;700&family=Source+Serif+4:wght@400&display=swap">
<style>
  :root{
    --ink:#4a4a4a;
    --ink-strong:#3d3d3d;
    --teal:#3fa9a6;
    --green:#6aab2e;
    --band:#dcedf7;
    --page:#ffffff;
  }
  *{box-sizing:border-box;margin:0;padding:0}
  html,body{width:1200px;height:507px;overflow:hidden;background:var(--page)}
  body{position:relative;font-family:"Quicksand",sans-serif;color:var(--ink)}
  .ad{position:absolute;top:136px;width:355px;height:276px;background:#fff;
      box-shadow:0 1px 5px rgba(0,0,0,.12);overflow:hidden}
  .ad--jubilee{left:26px}
  .ad--job{left:408px}
  .ad--advice{left:791px}
  .ad__photo{position:absolute;left:0;top:0;width:355px;height:235px}
  .brand{position:absolute;left:188px;top:12px;width:68px;height:68px;border-radius:50%;
      background:#fff;display:flex;align-items:center;justify-content:center;text-align:center;
      font-weight:600;font-size:7.4px;line-height:1.15;color:var(--ink-strong);letter-spacing:.2px}
  .ad__body{position:absolute;left:26px;top:27px;width:190px}
  .kicker{font-family:"Source Serif 4",serif;font-size:10.5px;line-height:13px;color:var(--ink)}
  .title{font-size:13.4px;font-weight:700;line-height:17px;color:var(--ink-strong);margin-top:4px}
  .title span{display:block;color:var(--teal)}
  .rule{width:50px;height:2px;background:var(--green);margin:6px 0 10px}
  .text{font-size:9px;line-height:13px;font-weight:500;white-space:nowrap}
  .text--small{font-size:8.3px;line-height:12.4px}
  .text b{font-weight:700;color:var(--ink-strong)}
  .sub{font-size:8.4px;line-height:12px;font-weight:700;color:var(--green);margin-top:7px}
  .sub--large{font-size:11.4px;line-height:14px;margin-top:12px}
  .list{list-style:none;margin-top:1px}
  .list li{position:relative;padding-left:10px;font-size:8.3px;line-height:12px;font-weight:500;white-space:nowrap}
  .list li::before{content:"+";position:absolute;left:0;color:var(--green);font-weight:700}
  .list--roomy{margin-top:3px}
  .list--roomy li{font-size:9.2px;line-height:15.6px}
  .list--gap{margin-top:10px}
  .list--gap li{font-size:9px;line-height:13.2px;margin-bottom:3px}
  .list--gap b{font-weight:700;color:var(--ink-strong)}
  .ad__footer{position:absolute;left:0;bottom:0;width:100%;height:41px;background:var(--band);
      display:flex;align-items:center;justify-content:space-between;padding:0 24px 0 22px}
  .footer__note{font-family:"Source Serif 4",serif;font-size:10.6px;color:var(--ink);white-space:nowrap}
  .footer__note--small{font-size:8.4px}
  .cta{background:var(--teal);color:#fff;font-weight:600;font-size:9px;border-radius:10px;
      padding:4px 9px;white-space:nowrap}
</style>
</head>
<body>

<svg width="0" height="0" style="position:absolute">
  <defs>
    <linearGradient id="tone-warm" x1="0" y1="0" x2="1" y2="1">
      <stop offset="0" stop-color="#e6d2bd"/><stop offset="1" stop-color="#8e7560"/>
    </linearGradient>
    <linearGradient id="tone-kitchen" x1="0" y1="0" x2="1" y2="1">
      <stop offset="0" stop-color="#c9c4bc"/><stop offset=".6" stop-color="#a7b79a"/><stop offset="1" stop-color="#5f5a52"/>
    </linearGradient>
    <linearGradient id="tone-living" x1="0" y1="0" x2="1" y2="1">
      <stop offset="0" stop-color="#e3e7e2"/><stop offset=".6" stop-color="#9fb3c2"/><stop offset="1" stop-color="#6d5a4c"/>
    </linearGradient>
  </defs>
</svg>

<!-- Jubiläum -->
<article class="ad ad--jubilee">
  <svg class="ad__photo" viewBox="0 0 355 235" role="img" aria-label="Foto: Pflegerin hält lächelnd die Hand einer Seniorin">
    <path d="M245 0 C205 60 200 170 222 235 L355 235 L355 0 Z" fill="url(#tone-warm)"/>
  </svg>
  <div class="brand">SORGSAM<br>PFLEGE</div>
  <div class="ad__body">
    <p class="kicker">Feiern Sie mit uns!</p>
    <h2 class="title">1-jähriges Jubiläum<span>am 01. September 2024</span></h2>
    <div class="rule"></div>
    <p class="text">Anlässig unseres 1-jährigen Jubiläums,<br>möchten wir uns bei allen <b>Patienten,</b><br><b>Angehörigen und Interessenten</b> für<br>das Vertrauen bedanken.</p>
    <p class="sub sub--large">Besuchen Sie uns:</p>
    <ul class="list list--roomy">
      <li>01. Septemer 2024, 10:00 Uhr – 15:00</li>
      <li>Lindenweg 14, Dessau-Roßlau</li>
      <li>Kostenlose Beratung vor Ort</li>
    </ul>
  </div>
  <footer class="ad__footer">
    <span class="footer__note">Wir freuen uns auf dich!</span>
    <span class="cta">www.sorgsam-pflege.de</span>
  </footer>
</article>

<!-- Stellenanzeige -->
<article class="ad ad--job">
  <svg class="ad__photo" viewBox="0 0 355 235" role="img" aria-label="Foto: Hauswirtschafterin mit Schürze in der Küche">
    <path d="M245 0 C205 60 200 170 222 235 L355 235 L355 0 Z" fill="url(#tone-kitchen)"/>
  </svg>
  <div class="brand">SORGSAM<br>PFLEGE</div>
  <div class="ad__body">
    <p class="kicker">Komm in unser Team!</p>
    <h2 class="title"><span>Hauswirtschafter/in</span></h2>
    <div class="rule"></div>
    <p class="text text--small">Hilf uns die Pflege in der Umgebung<br><b>Dessau-Roßlau</b> qualitativ zu verbessern<br>und menschlicher zu gestalten.</p>
    <p class="sub">Was bringst du mit</p>
    <ul class="list">
      <li>Hilfsbereitschaft &amp; Engagement</li>
      <li>Führerschein Klasse B</li>
      <li>Gute Deutschkenntnisse in Wort und Schrift</li>
    </ul>
    <p class="sub">Das bieten wir</p>
    <ul class="list">
      <li>30 Tage Urlaub</li>
      <li>Fort- &amp; Weiterbildungen, Sonderleistungen</li>
      <li>Überdurchschnittliche Vergütung</li>
    </ul>
  </div>
  <footer class="ad__footer">
    <span class="footer__note footer__note--small">Wir freuen uns auf deine Bewerbung!</span>
    <span class="cta">www.sorgsam-pflege.de/karriere</span>
  </footer>
</article>

<!-- Beratung -->
<article class="ad ad--advice">
  <svg class="ad__photo" viewBox="0 0 355 235" role="img" aria-label="Foto: lächelnde Seniorin mit Unterlagen im Wohnzimmer">
    <path d="M245 0 C205 60 200 170 222 235 L355 235 L355 0 Z" fill="url(#tone-living)"/>
  </svg>
  <div class="brand">SORGSAM<br>PFLEGE</div>
  <div class="ad__body">
    <p class="kicker">Lassen Sie sich beraten!</p>
    <h2 class="title">Beratungseinsatz<span>nach. §37 Abs. 3 SGB XI.</span></h2>
    <div class="rule"></div>
    <p class="text">Der Beratungseinsatz stellt sicher,<br>dass <b>Pflegegeldempfänger</b> regelmäßig<br>qualifiziert beraten werden.</p>
    <ul class="list list--gap">
      <li>Pflegebedürftige mit Pflegegeld <b>müssen</b><br><b>regelmäßig</b> eine Beratung erhalten.</li>
      <li>Ziel ist die Sicherstellung der <b>Pflegequalität</b><br><b>und die Unterstützung</b> (z. B. Pflegekurse,<br>Entlastungsmöglichkeiten <b>pflegender</b><br><b>Angehöriger.</b></li>
    </ul>
  </div>
  <footer class="ad__footer">
    <span class="footer__note">Nehmen Sie Kontakt mir auns auf!</span>
    <span class="cta">www.sorgsam-pflege.de</span>
  </footer>
</article>

</body>
</html>
```